Need a FLAT UI design for mobile campus Marketplace APP

We need to improve our current UI/UX design for a mobile application called Tradora. It is designed for students to buy and sell their goods, such as books and furnitures, on their own campus to save living expenses. Our initial design does not look very flat and clear enough. We would like to see a flat design improvement for a better purchasing and selling experience using yellow as theme color.

Target Market(s)

college students

Industry/Entity Type

Marketplace

Colors
ffc214
ffcf3e
fee18a
fff3d1

Requirements
Must have
• an improved UI look, flat and simple.
Nice to have
• alternative designs
Should not have
• a new function design for the app on the design

```html
<!DOCTYPE html>
<html lang="en">
<head>
<meta charset="utf-8">
<title>Tradora – Campus Marketplace</title>
<link rel="stylesheet" href="https://fonts.googleapis.com/css2?family=Open+Sans:wght@400;700;800&family=Roboto+Condensed:wght@300;400&display=swap">
<style>
  :root {
    --yellow: #ffc214;
    --yellow-mid: #ffcf3e;
    --yellow-soft: #fee18a;
    --yellow-pale: #fff3d1;
    --stage: #e5620f;
    --orange-type: #f0641e;
    --ink: #1d1d1d;
    --grey-text: #c9b98a;
    --tile: #ffffff;
    --tile-gap: #f3f3f3;
    --icon: #ffd52e;
  }
  * { box-sizing: border-box; margin: 0; padding: 0; }
  html, body {
    width: 1200px; height: 800px; overflow: hidden;
    background: var(--stage);
    font-family: "Open Sans", sans-serif;
  }
  .app-screen {
    position: absolute; left: 397px; top: 40px;
    width: 406px; height: 720px;
    background: var(--tile-gap);
    display: flex; flex-direction: column;
    overflow: hidden;
  }
  .search-bar {
    height: 62px; background: var(--yellow-soft);
    display: flex; align-items: center; gap: 14px;
    padding: 0 16px;
  }
  .search-bar .search-field {
    flex: 1; font-size: 15px; color: var(--grey-text);
    font-family: "Roboto Condensed", sans-serif; letter-spacing: .5px;
  }
  .add-button {
    width: 26px; height: 26px; border-radius: 50%;
    background: var(--yellow); display: flex; align-items: center; justify-content: center;
  }
  .promo-banner {
    position: relative; height: 248px;
    background: var(--yellow); padding: 10px 12px 14px;
  }
  .promo-photo {
    position: relative; width: 100%; height: 100%;
    background: radial-gradient(circle at 30% 70%, #b78457 0 14%, transparent 32%),
                linear-gradient(135deg, #9aa7e0 0%, #5a5a9a 40%, #2c2c4c 75%, #3e3e58 100%);
  }
  .promo-title {
    position: absolute; right: 18px; top: 18px; text-align: right;
    font-family: "Roboto Condensed", sans-serif; font-weight: 300;
  }
  .promo-brand { color: #fff; font-size: 22px; letter-spacing: 1px; }
  .promo-product { color: var(--orange-type); font-size: 54px; line-height: 1; letter-spacing: 1px; }
  .promo-ribbon {
    position: absolute; right: -12px; top: 118px;
    background: var(--yellow); color: var(--ink);
    font-family: "Roboto Condensed", sans-serif; font-weight: 400; font-size: 14px;
    padding: 5px 14px 5px 22px; letter-spacing: 1px;
    clip-path: polygon(0 0, 100% 0, 100% 100%, 0 100%, 12px 50%);
  }
  .carousel-dots {
    position: absolute; bottom: 14px; left: 0; right: 0;
    display: flex; justify-content: center; gap: 8px;
  }
  .carousel-dots span { width: 7px; height: 7px; border-radius: 50%; border: 1.5px solid #fff; }
  .carousel-dots span.is-active { background: #fff; }
  .category-grid {
    flex: 1; display: grid; grid-template-columns: repeat(3, 1fr); grid-template-rows: repeat(2, 1fr);
    gap: 6px; padding: 6px;
  }
  .category-tile {
    background: var(--tile); box-shadow: 0 1px 3px rgba(0,0,0,.08);
    position: relative; display: flex; align-items: center; justify-content: center;
  }
  .category-tile svg { margin-bottom: 26px; }
  .category-label {
    position: absolute; right: 10px; bottom: 10px;
    font-weight: 800; font-size: 11px; color: var(--ink); letter-spacing: .5px;
  }
  .tab-bar {
    height: 80px; background: #fff; border-top: 1px solid #eee;
    display: flex; align-items: center; justify-content: space-around; padding: 0 8px;
  }
  .tab-item {
    display: flex; flex-direction: column; align-items: center; gap: 4px;
    font-family: "Roboto Condensed", sans-serif; font-size: 11px; color: var(--ink); letter-spacing: .5px;
  }
  .tab-home {
    width: 56px; height: 56px; border-radius: 50%; background: var(--yellow-mid);
    display: flex; align-items: center; justify-content: center;
  }
  .tab-home-inner {
    width: 40px; height: 40px; border-radius: 50%; border: 2px solid #fff;
    display: flex; align-items: center; justify-content: center;
  }
</style>
</head>
<body>
<main class="app-screen">
  <header class="search-bar">
    <svg width="16" height="16" viewBox="0 0 16 16" fill="none" stroke="#fff" stroke-width="2.2"><circle cx="6.5" cy="6.5" r="4.5"/><path d="M10 10l4 4"/></svg>
    <span class="search-field">Headset</span>
    <span class="add-button"><svg width="12" height="12" viewBox="0 0 12 12" stroke="#fff" stroke-width="2.4"><path d="M6 1v10M1 6h10"/></svg></span>
  </header>

  <section class="promo-banner">
    <div class="promo-photo" role="img" aria-label="Product photo of over-ear headphones with tan ear cushions on a blurred blue background">
      <div class="promo-title">
        <div class="promo-brand">NOVA</div>
        <div class="promo-product">HEADSET</div>
      </div>
      <div class="carousel-dots"><span></span><span class="is-active"></span><span></span></div>
    </div>
    <div class="promo-ribbon">BRAND NEW</div>
  </section>

  <section class="category-grid">
    <div class="category-tile">
      <svg width="70" height="50" viewBox="0 0 70 50" fill="var(--icon)">
        <path d="M4 14l10-6 10 6v2H4z"/><rect x="6" y="17" width="16" height="8"/>
        <path d="M42 10l12-5 12 5-12 5z"/><rect x="48" y="12" width="12" height="6"/>
        <rect x="24" y="34" width="12" height="10"/><rect x="22" y="30" width="4" height="4"/>
        <rect x="48" y="34" width="16" height="8" rx="2"/>
      </svg>
      <span class="category-label">CAMPUS LIFE</span>
    </div>
    <div class="category-tile">
      <svg width="70" height="50" viewBox="0 0 70 50" fill="none" stroke="var(--icon)" stroke-width="2.5">
        <rect x="6" y="10" width="20" height="13"/><rect x="46" y="4" width="12" height="16"/>
        <circle cx="14" cy="38" r="5"/><rect x="42" y="32" width="20" height="8" rx="2"/>
      </svg>
      <span class="category-label">ELECTRONIC</span>
    </div>
    <div class="category-tile">
      <svg width="64" height="54" viewBox="0 0 64 54" fill="var(--icon)">
        <rect x="2" y="2" width="28" height="23"/><rect x="34" y="2" width="28" height="23"/>
        <rect x="2" y="29" width="28" height="23"/><rect x="34" y="29" width="28" height="23"/>
      </svg>
      <span class="category-label">RECENT</span>
    </div>
    <div class="category-tile">
      <svg width="56" height="44" viewBox="0 0 56 44" fill="none" stroke="var(--icon)" stroke-width="3">
        <path d="M4 6h18c3 0 6 3 6 6v28c0-3-3-5-6-5H4z"/><path d="M52 6H34c-3 0-6 3-6 6v28c0-3 3-5 6-5h18z"/>
      </svg>
      <span class="category-label">BOOKS</span>
    </div>
    <div class="category-tile">
      <svg width="60" height="36" viewBox="0 0 60 36" fill="var(--icon)">
        <path d="M2 4h56v9a5 5 0 000 10v9H2v-9a5 5 0 000-10z"/>
      </svg>
      <span class="category-label">TICKETS</span>
    </div>
    <div class="category-tile">
      <svg width="60" height="30" viewBox="0 0 60 30">
        <rect x="1" y="1" width="58" height="28" rx="3" fill="var(--icon)"/>
        <circle cx="16" cy="15" r="4" fill="#fff"/><circle cx="30" cy="15" r="4" fill="#fff"/><circle cx="44" cy="15" r="4" fill="#fff"/>
      </svg>
      <span class="category-label">OTHERS</span>
    </div>
  </section>

  <nav class="tab-bar">
    <div class="tab-item">
      <svg width="26" height="20" viewBox="0 0 26 20" fill="none" stroke="var(--icon)" stroke-width="2"><path d="M2 2h22v13H9l-5 4v-4H2z"/></svg>CHAT</div>
    <div class="tab-item">
      <svg width="28" height="20" viewBox="0 0 28 20" fill="none" stroke="var(--icon)" stroke-width="2"><path d="M6 18a5 5 0 010-10 7 7 0 0113-2 6 6 0 013 12z"/></svg>TRADE</div>
    <div class="tab-home"><div class="tab-home-inner">
      <svg width="18" height="18" viewBox="0 0 18 18" fill="#fff"><path d="M9 1l8 7h-2v9h-4v-5H7v5H3V8H1z"/></svg></div></div>
    <div class="tab-item">
      <svg width="22" height="20" viewBox="0 0 22 20" fill="none" stroke="var(--icon)" stroke-width="2"><rect x="2" y="3" width="16" height="15"/><path d="M8 12l11-10"/></svg>POST</div>
    <div class="tab-item">
      <svg width="22" height="20" viewBox="0 0 22 20"><circle cx="11" cy="10" r="9" fill="var(--icon)"/><circle cx="11" cy="8" r="3" fill="#fff"/><path d="M5 16a6 6 0 0112 0" fill="#fff"/></svg>PROFILE</div>
  </nav>
</main>
</body>
</html>
```